BUSINESS CARD FOR GUITAR SCHOOL

I would like to design a business card for my Guitar Music School. The school is called "Pluck & Lantern".

The card should be yellow.

Target Market(s)

18-35 years old

Industry/Entity Type

School

Contact Information for Business Card

I would like to design a business card for my Guitar Music School. The school is called "Pluck & Lantern". The card should be yellow.

Card must be consistent with my website design: www.pluckandlantern.com.sg

Requirements
Must have
• 1) Name of Company
• 2) Company Logo
• 3) Name of Employee
• 4) Position of Employee
• 5) Contact Number
• 6) Address
Nice to have
• Creative Design
• Card must be consistent with my website design: www.pluckandlantern.com.sg
Should not have
• Boring Design

```html
<!DOCTYPE html>
<html lang="en">
<head>
<meta charset="utf-8">
<title>Pluck &amp; Lantern – Business Card</title>
<link rel="stylesheet" href="https://fonts.googleapis.com/css2?family=Alfa+Slab+One&family=Ubuntu:wght@400&display=swap">
<style>
  :root {
    --card-yellow: #fcc12c;
    --note-yellow: #ffc900;
    --rule-yellow: #ffd21a;
    --paper: #ffffff;
    --ink-light: #ffffff;
    --ink-dark: #2b2a29;
    --icon-red: #e42427;
  }
  * { margin: 0; padding: 0; box-sizing: border-box; }
  html, body {
    width: 999px; height: 1200px; overflow: hidden;
    background: var(--paper);
  }
  .sheet { position: relative; width: 999px; height: 1200px; }
  .card {
    position: absolute; left: 0; width: 999px; height: 585px;
    background: var(--card-yellow); overflow: hidden;
    font-family: "Alfa Slab One", Georgia, serif;
    color: var(--ink-light);
  }
  .card--light { top: 0; }
  .card--dark { top: 613px; height: 587px; color: var(--ink-dark); }
  .card--dark .icon { fill: var(--icon-red); }
  .card--light .icon { fill: var(--ink-light); }

  .note-decoration {
    position: absolute; left: 580px; top: 100px; width: 370px; height: 400px;
    background: radial-gradient(closest-side at 45% 70%, rgba(255,201,0,0.9) 0%, rgba(255,201,0,0.45) 50%, rgba(255,201,0,0) 100%);
  }
  .brand {
    position: absolute; left: 0; width: 999px; top: 112px; text-align: center;
  }
  .brand__name { font-size: 46px; line-height: 56px; letter-spacing: 0.5px; }
  .brand__tagline {
    font-family: "Ubuntu", Arial, sans-serif; font-size: 13px; line-height: 16px;
    margin-top: 28px; letter-spacing: 0.2px;
  }
  .employee {
    position: absolute; left: 100px; width: 824px; top: 256px; text-align: center;
    padding-left: 24px;
  }
  .employee__name {
    font-size: 60px; line-height: 64px; letter-spacing: 1.5px; word-spacing: 8px;
    font-weight: 400;
  }
  .employee__position {
    font-size: 31px; line-height: 36px; margin-top: 12px;
    letter-spacing: 1px; word-spacing: 4px;
  }
  .contact { position: absolute; left: 117px; top: 415px; }
  .contact__row {
    display: flex; align-items: center; height: 48px; margin-bottom: 22px;
    font-size: 31px; letter-spacing: 0.8px; word-spacing: 4px;
  }
  .contact__row .icon { width: 36px; height: 44px; margin-right: 24px; flex: none; }
  .contact__row--address .icon { width: 50px; height: 48px; margin-right: 20px; }
  .card__rule {
    position: absolute; left: 50px; width: 888px; top: 559px; height: 2px;
    background: var(--rule-yellow);
  }
</style>
</head>
<body>
<main class="sheet">
  <section class="card card--light" aria-label="Business card, light text version">
    <div class="note-decoration" role="img" aria-label="Large faint music note decoration"></div>
    <header class="brand">
      <div class="brand__name">Pluck &amp; Lantern</div>
      <div class="brand__tagline">Where Every Chord Finds Its Voice</div>
    </header>
    <div class="employee">
      <h1 class="employee__name">Name of Employee</h1>
      <p class="employee__position">Position of Employee</p>
    </div>
    <div class="contact">
      <div class="contact__row contact__row--phone">
        <svg class="icon" viewBox="0 0 40 44" aria-hidden="true"><path d="M9 2 L15 2 L18 12 L13 16 C15 24 19 30 26 34 L31 30 L39 35 L37 42 C35 44 30 44 25 41 C14 35 6 25 3 13 C2 8 4 4 9 2 Z"/></svg>
        <span>Contact Number</span>
      </div>
      <div class="contact__row contact__row--address">
        <svg class="icon" viewBox="0 0 50 48" aria-hidden="true"><path d="M25 2 L49 24 L45 27 L25 9 L5 27 L1 24 Z M9 27 L25 13 L41 27 L41 47 L30 47 L30 34 L20 34 L20 47 L9 47 Z M36 6 L42 6 L42 15 L36 10 Z"/></svg>
        <span>Address</span>
      </div>
    </div>
    <div class="card__rule"></div>
  </section>

  <section class="card card--dark" aria-label="Business card, dark text version">
    <div class="note-decoration" role="img" aria-label="Large faint music note decoration"></div>
    <header class="brand">
      <div class="brand__name">Pluck &amp; Lantern</div>
      <div class="brand__tagline">Where Every Chord Finds Its Voice</div>
    </header>
    <div class="employee">
      <h1 class="employee__name">Name of Employee</h1>
      <p class="employee__position">Position of Employee</p>
    </div>
    <div class="contact">
      <div class="contact__row contact__row--phone">
        <svg class="icon" viewBox="0 0 40 44" aria-hidden="true"><path d="M9 2 L15 2 L18 12 L13 16 C15 24 19 30 26 34 L31 30 L39 35 L37 42 C35 44 30 44 25 41 C14 35 6 25 3 13 C2 8 4 4 9 2 Z"/></svg>
        <span>Contact Number</span>
      </div>
      <div class="contact__row contact__row--address">
        <svg class="icon" viewBox="0 0 50 48" aria-hidden="true"><path d="M25 2 L49 24 L45 27 L25 9 L5 27 L1 24 Z M9 27 L25 13 L41 27 L41 47 L30 47 L30 34 L20 34 L20 47 L9 47 Z M36 6 L42 6 L42 15 L36 10 Z"/></svg>
        <span>Address</span>
      </div>
    </div>
    <div class="card__rule"></div>
  </section>
</main>
</body>
</html>
```